Easy Business Card / Presentation Cover Design Project

We are looking for a business card design, covers for powerpoint presentations for investors, and possibly simple stationary for a Chicago real estate development firm. Our new logo is attached below.

We rehab and provide newly constructed homes. We are not a real estate brokerage firm (i.e., agents such as Meridale 47) and only operate in the Chicago area.

In terms of design, sophisticated and high end that would appeal to investors (theme should resemble investment banks, hedge funds, private equity rather than tech startup).

Target Market(s)

Investors, banks, financing sources

Industry/Entity Type

Real Estate

Requirements
Must have
• Two deliverables here. 1) Business card 2) Covers for powerpoint presentation.

Must be able to look sophisticated and high end when printed. Please think through the type of printing that will be needed. Would prefer something that can be printed in raised ink but digital is ok as well.

Will be printed on heavy paper.

Business Card: Horizontal Layout, no black backgrounds,

For presentation front cover, should include logo only. For back cover, should include contact info. Horizontal and should not contain any information that will need to be changed (i.e. date or client name)
Nice to have
• Would like to have the edges colored but not required. Please show multiple designs
Should not have
• Should not have any die cut or embossed type of designs. Shape should be standard size.

We are not a design firm, a retail firm, or a consumer product firm.

Please do not incorporate a house, buildings, etc. This must be very professional looking.

```html
<!DOCTYPE html>
<html lang="en">
<head>
<meta charset="utf-8">
<title>Larkmont Realty – Business Card</title>
<link rel="stylesheet" href="https://fonts.googleapis.com/css2?family=Lato:wght@400;700&display=swap">
<style>
  :root {
    --page: #e4e5e7;
    --card-top: #ffffff;
    --card-bottom: #e6e7e8;
    --ink: #2a2a2a;
    --ink-soft: #4a4a4a;
    --accent: #2a86d8;
    --accent-light: #5fb3ee;
    --band: #4b4c4e;
    --band-text: #c9cacc;
    --rule: #9a9b9d;
  }
  * { box-sizing: border-box; margin: 0; padding: 0; }
  html, body {
    width: 1200px; height: 901px; overflow: hidden;
    background: var(--page);
    font-family: "Lato", sans-serif;
  }
  .sheet {
    position: relative; width: 1200px; height: 901px;
    display: flex; align-items: center; justify-content: center; gap: 60px;
  }
  .card {
    position: relative; width: 520px; height: 297px;
    background: linear-gradient(180deg, var(--card-top), var(--card-bottom));
    box-shadow: 0 6px 18px rgba(0,0,0,.18);
    overflow: hidden;
  }

  /* front */
  .brand {
    position: absolute; left: 34px; top: 92px;
    display: flex; align-items: center; gap: 14px;
  }
  .brand-dot {
    width: 58px; height: 58px; border-radius: 50%;
    border: 4px solid var(--accent);
  }
  .brand-name {
    font-size: 30px; font-weight: 700; line-height: 1;
    color: var(--ink); letter-spacing: .5px;
  }
  .divider {
    position: absolute; left: 272px; top: 52px;
    width: 1px; height: 150px; background: var(--rule);
  }
  .contact { position: absolute; left: 292px; top: 54px; color: var(--ink); }
  .person-name { font-size: 17px; letter-spacing: .4px; text-transform: uppercase; }
  .person-role { font-size: 12px; color: var(--ink-soft); margin-bottom: 16px; }
  .contact-list { display: grid; grid-template-columns: 44px auto; row-gap: 2px; font-size: 12px; }
  .contact-list dt { color: var(--accent); text-align: right; padding-right: 6px; }
  .contact-list dd { color: var(--ink); }
  .contact-list .gap { margin-top: 12px; }
  .address-band {
    position: absolute; left: 0; right: 0; bottom: 0; height: 46px;
    background: var(--band); color: var(--band-text);
    font-size: 14px; letter-spacing: .4px;
    display: flex; align-items: center; padding-left: 148px;
  }

  /* back */
  .back-circle {
    position: absolute; left: -60px; top: 40px;
    width: 240px; height: 240px; border-radius: 50%;
    border: 10px solid var(--accent-light);
  }
  .back-name {
    position: absolute; right: 40px; top: 70px;
    font-size: 38px; font-weight: 700; line-height: 1;
    color: var(--ink); text-align: right;
  }
</style>
</head>
<body>
<main class="sheet">
  <section class="card card-front" aria-label="Business card front">
    <div class="brand">
      <span class="brand-dot"></span>
      <span class="brand-name">Larkmont<br>Realty</span>
    </div>
    <div class="divider"></div>
    <div class="contact">
      <p class="person-name">Daniel Whitcombe</p>
      <p class="person-role">managing director</p>
      <dl class="contact-list">
        <dt>phone</dt><dd>312 555 01 48</dd>
        <dt>cell</dt><dd>312 555 01 97</dd>
        <dt class="gap">email</dt><dd class="gap">info@larkmontrealty.com</dd>
        <dt>web</dt><dd>www.larkmontrealty.com</dd>
      </dl>
    </div>
    <div class="address-band">480 Harlow Avenue, Westbrook, Illinois 60612</div>
  </section>

  <section class="card card-back" aria-label="Business card back">
    <span class="back-circle"></span>
    <p class="back-name">Larkmont<br>Realty</p>
  </section>
</main>
</body>
</html>
```